We would like to develop 1x set of HTML5 banners of 3x formats (300x600, 640x270, 1170x340) to promote our website Inkleaf7.com. These banners will be displayed on the website pelmora.com.

We sell temporary tattoos. The goal is to drive traffic on our e-commerce website and generate sales. Please, find herewith our logo and a few pictures you can use in these banners.

The idea is to present 2-3 pictures of tattoos, add a promo code and a call-to-action.

- Main Message => Votre Tattoo Pas Pour La Vie
- Second Message => Livraison Gratuite & Rapide
- Promo => -20% sur toute la collection avec le code promo "pelmora20", valable jusqu'au 31 juillet 2019.
- Call-to-Action => Acheter Maintenant

```html
<!DOCTYPE html>
<html lang="fr">
<head>
<meta charset="utf-8">
<title>Inkleaf7 Banners</title>
<link rel="stylesheet" href="https://fonts.googleapis.com/css2?family=Oswald:wght@600&family=Poppins:wght@300;400&family=Ubuntu:wght@400;500&display=swap">
<style>
  :root {
    --sheet: #5f5f5f;
    --accent: #ff0a45;
    --white: #ffffff;
    --ink: #1b1b1b;
    --photo-dark: #2b3036;
    --photo-mid: #58616a;
    --photo-light: #8c959c;
    --rule: #d9d9d9;
  }
  * { box-sizing: border-box; margin: 0; padding: 0; }
  html, body { width: 1200px; height: 1200px; overflow: hidden; }
  body {
    position: relative;
    background: radial-gradient(circle at 50% 55%, #6a6a6a 0%, var(--sheet) 70%);
    font-family: "Ubuntu", sans-serif;
    color: var(--ink);
  }
  .edge { position: absolute; left: 0; width: 1200px; height: 8px; background: var(--accent); }
  .edge--top { top: 0; }
  .edge--bottom { bottom: 0; }

  .sheet-title {
    position: absolute; top: 80px; width: 100%; text-align: center;
    font-family: "Poppins", sans-serif; font-weight: 300; font-size: 25px;
    color: var(--white); letter-spacing: 0.5px;
  }
  .format-label {
    position: absolute; font-family: "Poppins", sans-serif; font-weight: 300;
    font-size: 16px; color: var(--white);
  }

  .banner { position: absolute; overflow: hidden; background: var(--white); box-shadow: 0 4px 14px rgba(0,0,0,0.25); }
  .photo { position: absolute; }
  .photo--arm { background: linear-gradient(120deg, var(--photo-light) 0%, var(--photo-mid) 40%, var(--photo-dark) 100%); }
  .photo--couple { background: linear-gradient(160deg, var(--photo-mid) 0%, var(--photo-dark) 55%, #3e5878 100%); }

  .frame { position: absolute; border: 1px solid rgba(255,255,255,0.55); pointer-events: none; }

  .brand {
    position: absolute; font-family: "Ubuntu", sans-serif; font-weight: 500;
    color: var(--white); white-space: nowrap;
  }

  .offer {
    position: absolute; display: flex; flex-direction: column; align-items: center;
    text-align: center; background: var(--white);
  }
  .offer__headline {
    font-family: "Oswald", sans-serif; font-weight: 600; font-style: italic;
    color: var(--accent); text-transform: uppercase; letter-spacing: 0.3px;
  }
  .offer__rule { background: var(--rule); height: 1px; }
  .offer__delivery { font-weight: 400; }
  .offer__promo { font-weight: 400; }
  .offer__promo em { font-style: normal; color: var(--accent); }
  .offer__code {
    background: var(--accent); color: var(--white); font-weight: 500;
    display: inline-block;
  }
  .offer__validity {
    font-family: "Oswald", sans-serif; font-weight: 600; font-style: italic;
    color: var(--accent); text-transform: uppercase;
  }

  .cta {
    position: absolute; background: var(--accent); color: var(--white);
    font-family: "Oswald", sans-serif; font-weight: 600; text-transform: uppercase;
    display: flex; align-items: center; white-space: nowrap;
  }
  .cta svg { margin-left: 3px; }

  /* 1170x340 */
  .banner--wide { left: 130px; top: 218px; width: 936px; height: 272px; }
  .banner--wide .photo--arm { left: 0; top: 0; width: 363px; height: 272px; }
  .banner--wide .photo--couple { left: 676px; top: 0; width: 260px; height: 272px; }
  .banner--wide .frame--left { left: 9px; top: 9px; width: 357px; height: 254px; }
  .banner--wide .frame--right { left: 672px; top: 9px; width: 255px; height: 210px; }
  .banner--wide .brand { left: 24px; top: 20px; font-size: 28px; }
  .banner--wide .offer { left: 363px; top: 0; width: 313px; height: 272px; padding-top: 20px; }
  .banner--wide .offer__headline { font-size: 38px; line-height: 38px; }
  .banner--wide .offer__rule { width: 200px; margin: 10px 0 6px; }
  .banner--wide .offer__delivery { font-size: 21px; line-height: 26px; }
  .banner--wide .offer__promo { font-size: 21px; line-height: 24px; margin-top: 9px; }
  .banner--wide .offer__code { font-size: 21px; line-height: 26px; padding: 0 12px; margin-top: 3px; }
  .banner--wide .offer__validity { font-size: 17px; margin-top: 10px; }
  .banner--wide .cta {
    left: 746px; top: 231px; width: 190px; height: 41px; padding-left: 30px; font-size: 15px;
    clip-path: polygon(16px 0, 100% 0, 100% 100%, 0 100%);
  }

  /* 640x270 */
  .banner--medium { left: 130px; top: 609px; width: 512px; height: 216px; }
  .banner--medium .photo--arm { left: 0; top: 0; width: 140px; height: 216px; }
  .banner--medium .photo--couple { left: 381px; top: 0; width: 131px; height: 216px; }
  .banner--medium .brand { left: 14px; top: 8px; font-size: 20px; }
  .banner--medium .offer { left: 140px; top: 0; width: 241px; height: 216px; padding-top: 22px; }
  .banner--medium .offer__headline { font-size: 29px; line-height: 29px; }
  .banner--medium .offer__rule { width: 170px; margin: 5px 0 4px; }
  .banner--medium .offer__delivery { font-size: 16px; line-height: 20px; }
  .banner--medium .offer__promo { font-size: 16px; line-height: 19px; margin-top: 7px; }
  .banner--medium .offer__code { font-size: 16px; line-height: 19px; padding: 0 9px; margin-top: 2px; }
  .banner--medium .offer__validity { font-size: 12.5px; margin-top: 8px; }
  .banner--medium .cta {
    left: 388px; top: 190px; width: 124px; height: 26px; padding-left: 18px; font-size: 10px;
    clip-path: polygon(10px 0, 100% 0, 100% 100%, 0 100%);
  }

  /* 300x600 */
  .banner--tall { left: 718px; top: 609px; width: 240px; height: 480px; }
  .banner--tall .photo--arm { left: 0; top: 0; width: 240px; height: 137px; }
  .banner--tall .photo--couple { left: 0; top: 338px; width: 240px; height: 142px; }
  .banner--tall .brand { right: 10px; top: 6px; font-size: 19px; }
  .banner--tall .offer { left: 0; top: 137px; width: 240px; height: 201px; padding-top: 15px; }
  .banner--tall .offer__headline { font-size: 27px; line-height: 27px; }
  .banner--tall .offer__rule { width: 180px; margin: 5px 0 4px; }
  .banner--tall .offer__delivery { font-size: 16px; line-height: 20px; }
  .banner--tall .offer__promo { font-size: 15.5px; line-height: 19px; margin-top: 8px; }
  .banner--tall .offer__code { font-size: 16px; line-height: 18px; padding: 0 9px; margin-top: 2px; }
  .banner--tall .offer__validity { font-size: 11px; margin-top: 8px; }
  .banner--tall .cta {
    left: 0; top: 449px; width: 148px; height: 31px; padding-left: 8px; font-size: 12px;
    clip-path: polygon(0 0, 136px 0, 100% 100%, 0 100%);
  }
</style>
</head>
<body>
  <div class="edge edge--top"></div>
  <div class="edge edge--bottom"></div>

  <h1 class="sheet-title">INKLEAF7 BANNERS</h1>

  <p class="format-label" style="left:130px;top:184px;">1170X340</p>
  <section class="banner banner--wide">
    <div class="photo photo--arm" role="img" aria-label="Photo of a man's heavily tattooed arm with skull artwork"></div>
    <div class="photo photo--couple" role="img" aria-label="Photo of a tattooed couple posing in front of a metal wall"></div>
    <div class="frame frame--left"></div>
    <div class="frame frame--right"></div>
    <div class="brand">Inkleaf7</div>
    <div class="offer">
      <h2 class="offer__headline">Votre tattoo pas<br>pour la vie</h2>
      <div class="offer__rule"></div>
      <p class="offer__delivery">Livraison Gratuite &amp; Rapide</p>
      <p class="offer__promo"><em>20%</em> sur toute la collection<br>avec le code promo</p>
      <span class="offer__code">pelmora20</span>
      <p class="offer__validity">Valable jusqu'au 31 juillet 2019.</p>
    </div>
    <a class="cta">Acheter maintenant
      <svg width="12" height="10" viewBox="0 0 12 10"><path d="M1 1l4 4-4 4M6 1l4 4-4 4" fill="none" stroke="#fff" stroke-width="1.6"/></svg>
    </a>
  </section>

  <p class="format-label" style="left:128px;top:576px;">640X270</p>
  <section class="banner banner--medium">
    <div class="photo photo--arm" role="img" aria-label="Photo of a man's heavily tattooed arm with skull artwork"></div>
    <div class="photo photo--couple" role="img" aria-label="Photo of a tattooed couple posing in front of a metal wall"></div>
    <div class="brand">Inkleaf7</div>
    <div class="offer">
      <h2 class="offer__headline">Votre tattoo pas<br>pour la vie</h2>
      <div class="offer__rule"></div>
      <p class="offer__delivery">Livraison Gratuite &amp; Rapide</p>
      <p class="offer__promo"><em>20%</em> sur toute la collection<br>avec le code promo</p>
      <span class="offer__code">pelmora20</span>
      <p class="offer__validity">Valable jusqu'au 31 juillet 2019.</p>
    </div>
    <a class="cta">Acheter maintenant
      <svg width="9" height="8" viewBox="0 0 12 10"><path d="M1 1l4 4-4 4M6 1l4 4-4 4" fill="none" stroke="#fff" stroke-width="1.8"/></svg>
    </a>
  </section>

  <p class="format-label" style="left:717px;top:576px;">300X600</p>
  <section class="banner banner--tall">
    <div class="photo photo--arm" role="img" aria-label="Photo of a man's heavily tattooed arm with skull artwork"></div>
    <div class="photo photo--couple" role="img" aria-label="Photo of a tattooed couple posing in front of a metal wall"></div>
    <div class="brand">Inkleaf7</div>
    <div class="offer">
      <h2 class="offer__headline">Votre tattoo pas<br>pour la vie</h2>
      <div class="offer__rule"></div>
      <p class="offer__delivery">Livraison Gratuite &amp; Rapide</p>
      <p class="offer__promo"><em>20%</em> sur toute la collection<br>avec le code promo</p>
      <span class="offer__code">pelmora20</span>
      <p class="offer__validity">Valable jusqu'au 31 juillet 2019.</p>
    </div>
    <a class="cta">Acheter maintenant
      <svg width="10" height="9" viewBox="0 0 12 10"><path d="M1 1l4 4-4 4M6 1l4 4-4 4" fill="none" stroke="#fff" stroke-width="1.7"/></svg>
    </a>
  </section>
</body>
</html>
```